Design some Business Cards

Will leave good review!
I need business cards with a logo and contact information.
This company name is Tidewell Plumbing Corp. Its a new Massachusetts plumbing business. Tidewell is phone area code in Massachusetts. Results have to look professional and clean. Please submit business card examples and logo ideas.
I was thinking Tidewell being designed as digits on the phone keys. Try to use a black background(with decorations or not), the rest being gold. Try to do a double sided design. Just large logo on one side, same slightly smaller logo and contact information on the other.

Lets go, we are getting there! I really like your ideas so far, thank you, I have more work to be done!
I will leave a 5 star review to the winner!

```html
<!DOCTYPE html>
<html lang="en">
<head>
<meta charset="UTF-8">
<title>Tidewell Plumbing Corp – Business Cards</title>
<link href="https://fonts.googleapis.com/css2?family=Oswald:wght@500&family=Roboto:wght@400;700&display=swap" rel="stylesheet">
<style>
  :root {
    --backdrop: #6f6d73;
    --card-black: #2a2a2a;
    --gold: #f0b323;
    --white: #ffffff;
    --muted: #d9d9d9;
  }
  * { margin: 0; padding: 0; box-sizing: border-box; }
  html, body { width: 1200px; height: 675px; overflow: hidden; }
  body {
    background: var(--backdrop);
    display: flex;
    align-items: center;
    justify-content: center;
    gap: 56px;
    font-family: "Roboto", sans-serif;
  }
  .card {
    width: 525px;
    height: 300px;
    background: var(--card-black);
    border-radius: 3px;
    box-shadow: 0 10px 24px rgba(0,0,0,0.35);
    position: relative;
    color: var(--white);
  }
  .brand-name {
    font-family: "Roboto", sans-serif;
    font-weight: 700;
    color: var(--white);
    line-height: 1.1;
  }

  /* Front side: contacts */
  .card-front .brand-name {
    position: absolute;
    left: 44px;
    top: 50%;
    transform: translateY(-50%);
    width: 190px;
    font-size: 24px;
  }
  .divider {
    position: absolute;
    left: 262px;
    top: 40px;
    bottom: 40px;
    width: 1px;
    background: linear-gradient(to bottom, transparent, var(--gold) 50%, transparent);
  }
  .contact-block {
    position: absolute;
    left: 290px;
    top: 58px;
  }
  .person-name {
    font-family: "Oswald", sans-serif;
    font-weight: 500;
    font-size: 20px;
    letter-spacing: 0.5px;
    text-transform: uppercase;
  }
  .person-title {
    font-size: 10px;
    color: var(--gold);
    letter-spacing: 1px;
    text-transform: uppercase;
    margin-top: 1px;
  }
  .contact-list {
    list-style: none;
    margin-top: 26px;
    font-size: 11.5px;
    color: var(--muted);
  }
  .contact-list li {
    display: flex;
    align-items: flex-start;
    gap: 8px;
    margin-bottom: 6px;
    line-height: 1.35;
  }
  .contact-list svg { width: 11px; height: 11px; flex: none; margin-top: 2px; }

  /* Back side: large name */
  .card-back { display: flex; align-items: center; justify-content: center; }
  .card-back .brand-name { font-size: 36px; text-align: center; }
</style>
</head>
<body>
  <section class="card card-front">
    <p class="brand-name">Tidewell Plumbing Corp</p>
    <div class="divider"></div>
    <div class="contact-block">
      <p class="person-name">Dale Mercer</p>
      <p class="person-title">Director</p>
      <ul class="contact-list">
        <li>
          <svg viewBox="0 0 24 24" fill="var(--gold)"><path d="M6.6 10.8a15.1 15.1 0 0 0 6.6 6.6l2.2-2.2a1 1 0 0 1 1-.25 11.4 11.4 0 0 0 3.6.57 1 1 0 0 1 1 1V20a1 1 0 0 1-1 1A17 17 0 0 1 3 4a1 1 0 0 1 1-1h3.5a1 1 0 0 1 1 1c0 1.25.2 2.45.57 3.57a1 1 0 0 1-.25 1z"/></svg>
          <span>555.0100-0199</span>
        </li>
        <li>
          <svg viewBox="0 0 24 24" fill="none" stroke="var(--gold)" stroke-width="2.4"><circle cx="12" cy="12" r="9"/><path d="M3 12h18M12 3c3 3.5 3 14.5 0 18M12 3c-3 3.5-3 14.5 0 18"/></svg>
          <span>www.tidewellplumbing.com</span>
        </li>
        <li>
          <svg viewBox="0 0 24 24" fill="var(--gold)"><path d="M12 2a7 7 0 0 0-7 7c0 5.2 7 13 7 13s7-7.8 7-13a7 7 0 0 0-7-7zm0 9.5A2.5 2.5 0 1 1 12 6.5a2.5 2.5 0 0 1 0 5z"/></svg>
          <span>42 Harbor Lane, 2nd Floor<br>Quincy, MA 02169</span>
        </li>
      </ul>
    </div>
  </section>

  <section class="card card-back">
    <p class="brand-name">Tidewell Plumbing Corp</p>
  </section>
</body>
</html>
```